Copper Lantern Design

Query ArtFolkHub: THE COPPER LANTERN FOLD
(commercial fiction, 85,000 words)

AUTHOR: Perry O. Vantosk [pen name] Author: Owen Felix Garrod
Tovah Quarme

Mass shooter, quadroon Lyle Pennicott, schools reporter Rosalind Okafor. Jewish commodity trader, Ari Kupferman, schools his trading partner, Neil Harrow, on how it feels to be a minority. Pennicott’s shooting lands Ari in a coma, and they all school each other. How did they get so ignorant? And about what? Trading, i.e., capitalism. Politics, i.e., corruption. Killing, i.e., war. The stuff you only say in public, never with a friend of another ethnicity, i.e., racism. Therefore, the topic of this novel is allodoxaphobia. [stay with me]

How many gears does an Italian tank have? It’s got nineteen in reverse and one in forward in case the enemy attacks from the rear. If ethnic comedy is offensive, you might have caught allodoxaphobia.

Allodoxaphobia? A plague spreads unseen through America. It’s faced by a financial wizard [Jew boy], his partner [Whitey], and an African-American news lady. Three subcultures face allodoxaphobia—fear of conflicting opinions.

Rosalind Okafor is sent with Hugh “Badger” Tolliver to cover a mass shooting in the Jewish suburb of Highland Park. KRT news gets her to take commodity trader, Neil Harrow, to interview the quadroon shooter, Lyle Pennicott, who justifies himself with brutal, woke truth that forces Rosalind to drop every racial inhibition and engage the Whitey with a variety of inappropriate interracial topics. Neil’s Jewish trading partner, Ari Kupferman, cannot be interviewed due to his coma.

Shooter, Pennicott, opens the door to the issues—war, capitalism, corruption, and race. All the issues climax at Ari’s memorial and Shiva.

Neil and Rosalind eventually turn romantic and the tension of the issues builds. Lyle is shown to be a troubled shooter but not the killer. Ari’s brother has the fake art, “Dusk over Tiberas,” and the KRT mole, a buxom beauty, uncovers corruption in the Lakeshore Constabulary.

QUALIFICATION? Garrod’s childhood gets the blame—the Jim Crow South and the bazaars of Kabul, Afghanistan. Garrod drove a bus on the Southside of Chicago, listened to innocent criminals for half a decade as a jail guard, then spent his careen trading in the pits of the Grain Exchange Hall. Hot tip from the floor: THE CROWD IS ALWAYS WRONG. It took Garrod a couple of years to understand the meme, and a couple decades to resolve the themes of this novel.

WRITINGS His memoir, Prayers at the Bell, was published by Harrowgate, and he wrote Voice of the Riverbank, the memoir of an Amazon shaman. (both have sold about 40,000) He’s a member of Paul Denvick’s Floor Sage series.

COMPARABLES: (You’ll know this better than I)
Hollis’s Tobias Reed for its emotional connections [and maybe racial language]
Varnetsky’s Sisters Belorova, The spiritual themes are not as overt as Varnetsky’s, but the undercurrent is audible for those with “ears to hear.”
Henry Falstow's 2061 is more political and graphic. Nevertheless, child rape is graphic
Pemberly, “A Winter Ballad”
Walter Pruett’s, Edge of the Marsh
Brewster’s, “Keeper of the Gulls,”

Best regards,
Owen Garrod
https://owengarrodwrites.example/

Target Market(s)

African American, Jewish, manorities, academics, home schoolers

Industry/Entity Type

SIZE -- approx 9 X 6

Requirements
Must have
• you can choose this
Nice to have
• I've sent many pictures and descriptions of the novel
Should not have
• foul or off color pics

```html
<!DOCTYPE html>
<html lang="en">
<head>
<meta charset="utf-8">
<title>The Copper Lantern Fold — Cover</title>
<link rel="stylesheet" href="https://fonts.googleapis.com/css2?family=Libre+Caslon+Text:wght@700&family=Archivo:wght@600&display=swap">
<style>
  :root {
    --backdrop: #e3e4e6;
    --ink: #111114;
    --paper: #ece9e2;
    --slate: #8f949c;
    --navy: #1f3252;
    --steel: #4c6688;
    --crimson: #8e1f26;
  }
  * { margin: 0; padding: 0; box-sizing: border-box; }
  html, body {
    width: 1200px;
    height: 1130px;
    overflow: hidden;
    background: var(--backdrop);
  }
  .canvas {
    position: relative;
    width: 1200px;
    height: 1130px;
    display: flex;
    align-items: center;
    justify-content: center;
  }
  .cover {
    position: relative;
    width: 660px;
    height: 990px;
    overflow: hidden;
    background: var(--paper);
  }
  .cover-art {
    position: absolute;
    inset: 0;
    width: 100%;
    height: 100%;
  }
  .cover-title {
    position: absolute;
    top: 150px;
    left: 0;
    right: 0;
    text-align: center;
    font-family: "Libre Caslon Text", Georgia, serif;
    font-weight: 700;
    font-size: 78px;
    line-height: 0.92;
    color: var(--ink);
    letter-spacing: -0.5px;
  }
  .cover-title span { display: block; }
  .cover-author {
    position: absolute;
    top: 770px;
    left: 250px;
    width: 340px;
    text-align: center;
    font-family: "Archivo", Arial, sans-serif;
    font-weight: 600;
    font-size: 44px;
    line-height: 1.08;
    color: var(--ink);
  }
</style>
</head>
<body>
<main class="canvas">
  <article class="cover">
    <svg class="cover-art" viewBox="0 0 660 990" role="img" aria-label="Cubist-style painted illustration of three faces in profile, a man, a woman and a young man, split by a crack, among shattered geometric shards in grey, navy and crimson">
      <defs>
        <linearGradient id="artTone" x1="0" y1="0" x2="1" y2="1">
          <stop offset="0" stop-color="#9aa0a8"/>
          <stop offset="0.28" stop-color="#e4e1da"/>
          <stop offset="0.5" stop-color="#6d7f99"/>
          <stop offset="0.66" stop-color="#a34a4c"/>
          <stop offset="0.8" stop-color="#e2ddd4"/>
          <stop offset="1" stop-color="#2a3a58"/>
        </linearGradient>
      </defs>
      <rect width="660" height="990" fill="url(#artTone)"/>
    </svg>
    <h1 class="cover-title">
      <span>The</span>
      <span>Copper</span>
      <span>Lantern</span>
      <span>Fold</span>
    </h1>
    <p class="cover-author">Owen Felix Garrod</p>
  </article>
</main>
</body>
</html>
```